Amazing new protein bar on the market - be a part of something special

We need packaging design for the wrapper for great tasting new protein. The product is called "Copperleaf Crisp". The packaging should have a modern font and design I catching - Copperleaf Crisp. If possible we would like to incorporate a picture of the bar in the background. The font and name of the bar should stand out and jump out at you. Modern font is a must. The product run will be blueberry - pomegranate. Please use bright colors, White, Red and/or Orange. Lightning bolts would be a plus.
Updates

Project Deadline Extended Reason: We have changed our product name. Would like to see more designs. Added Monday, April 17, 2017

Target Market(s)

Athletes, people on the go or on a diet

Industry/Entity Type

Product

Logo Text

Copperleaf Crisp

Colors
f04a51
f68e4e
faa54b
ffffff

Requirements
Must have
• Prefer modern font that jumps out at you. Slanted if possible
• Please use bright colors White, Red and/or Orange

```html
<!DOCTYPE html>
<html lang="en">
<head>
<meta charset="utf-8">
<title>Copperleaf Crisp — Blueberry-Pomegranate Wrapper</title>
<link rel="stylesheet" href="https://fonts.googleapis.com/css2?family=Archivo+Black&family=Archivo:wght@700;800&display=swap">
<style>
  :root {
    --stage: #e8430c;
    --wrapper-red: #e3101e;
    --wrapper-red-dark: #c10a16;
    --foil: #d9d9db;
    --foil-light: #eeeef0;
    --photo-top: #f2efec;
    --photo-bar: #e6b590;
    --badge: #1e1e1e;
    --ink: #111111;
    --white: #ffffff;
    --accent: #ffb21a;
  }
  html, body {
    margin: 0;
    padding: 0;
    width: 1200px;
    height: 971px;
    overflow: hidden;
    background: var(--stage);
  }
  .canvas {
    position: relative;
    width: 1200px;
    height: 971px;
  }
  .wrapper-art {
    position: absolute;
    left: 0;
    top: 0;
  }
  .brand-name {
    font-family: "Archivo Black", "Arial Black", sans-serif;
    fill: var(--white);
  }
  .flavour {
    font-family: "Archivo", Arial, sans-serif;
    font-weight: 800;
    fill: var(--ink);
    stroke: var(--white);
    stroke-width: 3;
    paint-order: stroke;
  }
  .badge-text {
    font-family: "Archivo", Arial, sans-serif;
    font-weight: 800;
    fill: var(--white);
  }
  .protein {
    font-family: "Archivo Black", "Arial Black", sans-serif;
    fill: var(--ink);
  }
  .protein-label, .net-weight {
    font-family: "Archivo", Arial, sans-serif;
    font-weight: 800;
    fill: var(--ink);
  }
</style>
</head>
<body>
<main class="canvas">
  <svg class="wrapper-art" width="1200" height="971" viewBox="0 0 1200 971" xmlns="http://www.w3.org/2000/svg">
    <defs>
      <linearGradient id="foilGrad" x1="0" y1="0" x2="0" y2="1">
        <stop offset="0" stop-color="var(--foil-light)"/>
        <stop offset="1" stop-color="var(--foil)"/>
      </linearGradient>
      <linearGradient id="photoGrad" x1="0" y1="0" x2="0" y2="1">
        <stop offset="0" stop-color="var(--photo-top)"/>
        <stop offset="0.35" stop-color="var(--photo-bar)"/>
        <stop offset="0.6" stop-color="#dcc3b0"/>
        <stop offset="1" stop-color="#ece9e6"/>
      </linearGradient>
    </defs>

    <!-- end seals -->
    <rect class="seal seal-left" x="113" y="304" width="64" height="349" fill="var(--wrapper-red-dark)"/>
    <rect class="seal seal-right" x="1006" y="304" width="81" height="349" fill="var(--wrapper-red-dark)"/>

    <!-- main front panel -->
    <rect class="panel-foil" x="177" y="304" width="829" height="349" fill="url(#foilGrad)"/>
    <polygon class="panel-red" points="177,304 655,304 655,505 177,590" fill="var(--wrapper-red)"/>

    <!-- product photo area -->
    <rect class="product-photo" role="img" aria-label="Photo of the blueberry-pomegranate protein bar with yogurt drizzle and fresh berries"
          x="655" y="326" width="225" height="300" fill="url(#photoGrad)"/>

    <!-- brand name -->
    <g class="brand-lockup" transform="rotate(-9 420 450)">
      <text class="brand-name" x="222" y="432" font-size="56" textLength="395" lengthAdjust="spacingAndGlyphs">COPPERLEAF</text>
      <text class="brand-name" x="222" y="508" font-size="76" textLength="235" lengthAdjust="spacingAndGlyphs">CRISP</text>
      <rect class="brand-mark" x="476" y="458" width="36" height="36" fill="var(--accent)"/>
    </g>

    <!-- flavour -->
    <g class="flavour-line" transform="rotate(-9 420 530)">
      <text class="flavour" x="232" y="540" font-size="26" textLength="385" lengthAdjust="spacingAndGlyphs">BLUEBERRY - POMEGRANATE</text>
      <text class="flavour" x="617" y="570" font-size="26" text-anchor="end">FLAVOURED</text>
    </g>

    <!-- claim badges -->
    <g class="claims">
      <circle cx="911" cy="367" r="29" fill="var(--badge)" stroke="var(--white)" stroke-width="3"/>
      <text class="badge-text" x="911" y="364" font-size="10.5" text-anchor="middle">GLUTEN</text>
      <text class="badge-text" x="911" y="377" font-size="10.5" text-anchor="middle">FREE</text>

      <circle cx="911" cy="431" r="29" fill="var(--badge)" stroke="var(--white)" stroke-width="3"/>
      <text class="badge-text" x="911" y="421" font-size="10.5" text-anchor="middle">NO</text>
      <text class="badge-text" x="911" y="434" font-size="10.5" text-anchor="middle">ADDED</text>
      <text class="badge-text" x="911" y="447" font-size="10.5" text-anchor="middle">SUGAR</text>

      <circle cx="911" cy="496" r="29" fill="var(--badge)" stroke="var(--white)" stroke-width="3"/>
      <text class="badge-text" x="911" y="493" font-size="10.5" text-anchor="middle">LOW</text>
      <text class="badge-text" x="911" y="506" font-size="10.5" text-anchor="middle">CALORIE</text>
    </g>

    <!-- protein & weight -->
    <text class="protein" x="911" y="572" font-size="26" text-anchor="middle">10G</text>
    <text class="protein-label" x="911" y="586" font-size="11" text-anchor="middle">PROTEIN</text>
    <text class="net-weight" x="911" y="603" font-size="11" text-anchor="middle">NET WT 60G</text>
  </svg>
</main>
</body>
</html>
```